Commercial Landscaping Flyer Needed

Looking for a flyer design to showcase what we offer for commercial landscape Installations. We want this to illustrate what sets us apart from our competitors. Include our EMR Safety rating of .72, that our average commercial landscape installation size is $215,000 with our largest completed in 2020 being $1,375,590. We have backgrounds in commercial design and installation and help our customers with Value Engineering Strategies. Since incorporating in 2005, we have an average employment retention length of 8 years. We want this flyer to show our commercial clients that we mean business and are dedicated to making their project happen on time, run efficiently, and we do excellent work.

Need extra days to review

```html
<!DOCTYPE html>
<html lang="en">
<head>
<meta charset="utf-8">
<title>Greenfield Grounds – Commercial Landscape Installations</title>
<link rel="stylesheet" href="https://fonts.googleapis.com/css2?family=Crimson+Text:wght@400;600;700&display=swap">
<style>
  :root {
    --lime: #c4d92f;
    --sage: #699b68;
    --forest: #03531f;
    --ink: #1b1c1b;
    --cream: #ffffff;
    --bar: #0b5e28;
  }
  * { margin: 0; padding: 0; box-sizing: border-box; }
  html, body { width: 927px; height: 1200px; overflow: hidden; background: var(--ink); }
  body { font-family: "Crimson Text", Georgia, serif; color: var(--cream); }

  .flyer { position: relative; width: 927px; height: 1200px; overflow: hidden; }

  .hero-photo {
    position: absolute; inset: 0;
    background:
      linear-gradient(180deg, #2a302c 0%, #3b423a 30%, #4a4e3a 50%, #3a3d30 60%, #262825 100%);
  }
  .hero-shade { position: absolute; inset: 0; }

  .stat-column {
    position: absolute; left: 41px; top: 0; width: 312px; height: 1044px;
    background: var(--forest);
  }
  .stat-column svg { position: absolute; left: 0; top: 0; }

  .brand {
    position: absolute; left: 0; top: 78px; width: 312px;
    display: flex; align-items: center; justify-content: center; gap: 10px;
    color: var(--lime); font-weight: 700; font-size: 30px; line-height: 1;
  }
  .brand-dot { width: 18px; height: 18px; border-radius: 50%; background: var(--lime); }

  .safety { position: absolute; left: 30px; top: 290px; display: flex; align-items: flex-start; }
  .safety-figure {
    color: var(--lime); font-size: 128px; line-height: 1; letter-spacing: -2px;
  }
  .safety-label {
    margin-left: 16px; margin-top: 10px;
    color: var(--lime); font-size: 25px; line-height: 35px;
  }

  .stat-card {
    position: absolute; left: 26px; width: 253px; height: 232px;
    background: var(--sage); border-radius: 3px;
    display: flex; flex-direction: column; align-items: center; justify-content: center;
    text-align: center; padding: 0 12px;
  }
  .stat-card--average { top: 471px; }
  .stat-card--largest { top: 759px; }
  .stat-value { color: var(--lime); font-weight: 700; font-size: 40px; line-height: 1.05; }
  .stat-card--largest .stat-value { font-size: 41px; }
  .stat-caption { font-size: 21px; line-height: 29px; margin-top: 4px; }

  .pitch { position: absolute; left: 435px; top: 760px; width: 452px; text-align: justify; }
  .pitch-headline { color: var(--lime); font-size: 24px; line-height: 33px; font-weight: 400; }
  .pitch-body { font-size: 21px; line-height: 30px; margin-top: 31px; }
  .pitch-body + .pitch-body { margin-top: 30px; text-align: left; }

  .contact-band {
    position: absolute; left: 0; top: 1095px; width: 927px; height: 105px;
    background: var(--sage);
  }
  .contact-block {
    position: absolute; top: 16px; padding-left: 22px;
    font-size: 20px; line-height: 29px;
  }
  .contact-block::before {
    content: ""; position: absolute; left: 0; top: 2px; width: 5px; height: 78px;
    background: var(--bar); border-radius: 3px;
  }
  .contact-block--online { left: 52px; }
  .contact-block--postal { left: 596px; }
</style>
</head>
<body>
<main class="flyer">
  <div class="hero-photo" role="img" aria-label="Aerial view of a city block with a modern yellow and grey apartment building and a landscaped rooftop courtyard"></div>
  <svg class="hero-shade" width="927" height="1200" viewBox="0 0 927 1200" aria-hidden="true">
    <polygon points="354,703 927,552 927,1200 0,1200 0,795 354,703" fill="#1c1d1c" opacity="0.85"/>
  </svg>

  <section class="stat-column">
    <svg width="312" height="260" viewBox="0 0 312 260" aria-hidden="true">
      <polygon points="0,0 312,0 312,168 157,254 0,168" fill="var(--sage)"/>
    </svg>
    <div class="brand"><span class="brand-dot"></span><span class="brand-name">Greenfield Grounds</span></div>

    <div class="safety">
      <span class="safety-figure">.72</span>
      <span class="safety-label">EMR<br>Safety<br>Rating</span>
    </div>

    <div class="stat-card stat-card--average">
      <p class="stat-value">$215,000</p>
      <p class="stat-caption">Average commercial landscape installation size</p>
    </div>

    <div class="stat-card stat-card--largest">
      <p class="stat-value">$1,375,590</p>
      <p class="stat-caption">Largest completed in<br>2020</p>
    </div>
  </section>

  <section class="pitch">
    <h1 class="pitch-headline">Dedicated in making your project happen on time and run efficiently</h1>
    <p class="pitch-body">We have backgrounds in commercial design and installation and help our customers with Value Engineering Strategies.</p>
    <p class="pitch-body">Since incorporating in 2005, we have an average employment retention length of 8 years.</p>
  </section>

  <footer class="contact-band">
    <address class="contact-block contact-block--online" style="font-style:normal">
      abc@website.com<br>www.website.com<br>+1 123456789
    </address>
    <address class="contact-block contact-block--postal" style="font-style:normal">
      Address line 1<br>Address Line 2, city,&nbsp; State<br>PO Box 123456
    </address>
  </footer>
</main>
</body>
</html>
```